Artificial Intelligence based service LanePilot.ai

Looking for a website for service designed for driving schools to deliver AI based solutions and features. File are to include various pages from contact to list of services to faqs, demos and more. we are looking for a website for AI based service for driving schools. services will include things like chat bots, voice agent, document processing and ai based marketing.

Target Market(s)

driving school owners and managers.

Industry/Entity Type

software and AI

Number of Pages Required

4 page

Font styles to use
Sans Serif

Requirements
Must have
• clean and easy to navigate pages. responsive. also delivery via FIGMA.

```html
<!DOCTYPE html>
<html lang="en">
<head>
<meta charset="utf-8">
<title>LanePilot.ai – Demo &amp; Contact</title>
<link href="https://fonts.googleapis.com/css2?family=Catamaran:wght@700;800&family=Nunito+Sans:wght@400;700&display=swap" rel="stylesheet">
<style>
  :root{
    --navy:#0c2249;
    --navy-btn:#03214d;
    --cta:#124a6e;
    --grad-start:#0b2447;
    --grad-end:#3a8fd0;
    --section-grey:#f8f8f8;
    --white:#ffffff;
    --text:#222222;
    --muted:#555555;
    --border:#dcdcdc;
    --select-bg:#e9e8ed;
    --footer-bg:#333333;
    --footer-head:#6abf5e;
    --footer-link:#cfcfcf;
    --logo-accent:#5cb85c;
  }
  *{box-sizing:border-box;margin:0;padding:0}
  html,body{width:734px;height:1200px;overflow:hidden;background:var(--white)}
  body{position:relative;font-family:"Nunito Sans",sans-serif;color:var(--text)}
  .abs{position:absolute}

  /* header */
  .site-header{left:0;top:0;width:734px;height:46px;background:var(--white)}
  .brand{left:52px;top:14px;display:flex;align-items:center;gap:4px;font-size:11px;font-weight:700;color:var(--navy);line-height:16px}
  .brand-dot{width:6px;height:6px;background:var(--logo-accent)}
  .main-nav a{position:absolute;top:18px;font-size:8.3px;line-height:12px;color:#333;text-decoration:none}
  .btn-demo{left:614px;top:11px;width:59px;height:24px;border-radius:3px;background:var(--cta);color:var(--white);font-size:8.8px;font-weight:700;display:flex;align-items:center;justify-content:center}
  .header-band{left:0;top:46px;width:734px;height:10.5px;background:linear-gradient(90deg,var(--grad-start),var(--grad-end))}

  /* section titles */
  .section-title{left:0;width:734px;text-align:center;font-family:"Catamaran",sans-serif;font-weight:800;font-size:19.5px;line-height:24px;color:var(--navy)}
  .section-lead{left:0;width:734px;text-align:center;font-size:8.3px;line-height:12px;color:var(--muted)}

  .demo-section{left:0;top:56.5px;width:734px;height:579.5px;background:var(--section-grey)}
  .card{background:var(--white);border-radius:4px}
  .demo-card{left:160px;top:170px;width:420px;height:424px}
  .contact-card{left:212.5px;top:714.5px;width:315px;height:382px;box-shadow:0 0 6px rgba(0,0,0,.05)}
  .card-title{left:160px;width:420px;text-align:center;font-weight:700;font-size:9.7px;line-height:12px;color:var(--text)}
  .card-lead{left:160px;width:420px;text-align:center;font-size:8.3px;line-height:12px;color:var(--text)}

  .field-label{font-size:8.3px;line-height:12px;color:var(--text)}
  .field{background:var(--white);border:0.6px solid var(--border);border-radius:3px}
  .select{background:var(--select-bg);border:0.6px solid var(--border);border-radius:3px;font-size:8.5px;line-height:24px;padding-left:6.5px;color:#111}
  .select svg{position:absolute;right:5px;top:9.5px}
  .submit{background:var(--navy-btn);border-radius:2px;color:var(--white);font-size:6.8px;font-weight:700;display:flex;align-items:center;justify-content:center}
  .resize-grip{right:2px;bottom:2px}

  /* footer */
  .site-footer{left:0;top:1097.6px;width:734px;height:110px;background:var(--footer-bg)}
  .footer-head{font-weight:700;font-size:9.7px;line-height:12px;color:var(--footer-head)}
  .footer-link{font-size:8.3px;line-height:12px;color:var(--footer-link)}
  .footer-text{font-size:8.3px;line-height:14.1px;color:var(--white)}
  .footer-contact{font-size:8.3px;line-height:12px;color:var(--white)}
</style>
</head>
<body>

<header class="abs site-header">
  <div class="abs brand"><span class="brand-dot"></span>LanePilot.ai</div>
  <nav class="main-nav">
    <a style="left:247px">Solutions</a>
    <a style="left:297px">Features</a>
    <a style="left:344px">Benefits</a>
    <a style="left:388px">Pricing</a>
    <a style="left:429px">FAQ</a>
    <a style="left:460px">Contact</a>
  </nav>
  <div class="abs btn-demo">Get Demo</div>
</header>
<div class="abs header-band"></div>

<section class="abs demo-section"></section>
<h2 class="abs section-title" style="top:96px">See It in Action</h2>
<p class="abs section-lead" style="top:131px">Experience how our AI solutions can transform your driving school.</p>

<div class="abs card demo-card"></div>
<h3 class="abs card-title" style="top:188px">Request a Free Demo</h3>
<p class="abs card-lead" style="top:213px">Fill out this form to schedule a personalized demo of our AI solutions for your driving school.</p>

<label class="abs field-label" style="left:175.5px;top:242.5px">Your Name</label>
<div class="abs field" style="left:175.5px;top:259px;width:389px;height:24.5px"></div>
<label class="abs field-label" style="left:175.5px;top:294.7px">Driving School Name</label>
<div class="abs field" style="left:175.5px;top:312px;width:389px;height:24px"></div>
<label class="abs field-label" style="left:175.5px;top:348px">Email Address</label>
<div class="abs field" style="left:175.5px;top:364.5px;width:389px;height:24px"></div>
<label class="abs field-label" style="left:175.5px;top:400.5px">Phone Number</label>
<div class="abs field" style="left:175.5px;top:417px;width:389px;height:24.5px"></div>
<label class="abs field-label" style="left:175.5px;top:453.6px">Approximate Monthly Students</label>
<div class="abs select" style="left:175.5px;top:470px;width:389px;height:24.5px">1-50
  <svg width="6" height="4" viewBox="0 0 6 4"><path d="M.8.8 3 3 5.2.8" fill="none" stroke="#111" stroke-width="1"/></svg></div>
<label class="abs field-label" style="left:175.5px;top:506px">Primary Interest</label>
<div class="abs select" style="left:175.5px;top:523px;width:389px;height:24.5px">Voice Agent
  <svg width="6" height="4" viewBox="0 0 6 4"><path d="M.8.8 3 3 5.2.8" fill="none" stroke="#111" stroke-width="1"/></svg></div>
<div class="abs submit" style="left:175.5px;top:558.5px;width:389px;height:20.5px">Request Demo</div>

<h2 class="abs section-title" style="top:641px">Contact Us</h2>
<p class="abs section-lead" style="top:676px">Have questions? Our team is ready to help you find the right solutions for your driving school.</p>

<div class="abs card contact-card"></div>
<label class="abs field-label" style="left:233.5px;top:737px">Name</label>
<div class="abs field" style="left:233.5px;top:753.5px;width:273px;height:24.5px"></div>
<label class="abs field-label" style="left:233.5px;top:790px">Email</label>
<div class="abs field" style="left:233.5px;top:806.6px;width:273px;height:24px"></div>
<label class="abs field-label" style="left:233.5px;top:843px">Phone</label>
<div class="abs field" style="left:233.5px;top:858.8px;width:273px;height:24.5px"></div>
<label class="abs field-label" style="left:233.5px;top:895px">Driving School (if applicable)</label>
<div class="abs field" style="left:233.5px;top:912px;width:273px;height:24px"></div>
<label class="abs field-label" style="left:233.5px;top:948px">Message</label>
<div class="abs field" style="left:233.5px;top:964.6px;width:273px;height:78.5px">
  <svg class="abs resize-grip" width="6" height="6" viewBox="0 0 6 6"><path d="M5.5 1 1 5.5M5.5 3 3 5.5M5.5 5 5 5.5" stroke="#888" stroke-width=".6"/></svg>
</div>
<div class="abs submit" style="left:233.5px;top:1055.7px;width:273px;height:20.5px">Send Message</div>

<footer class="abs site-footer"></footer>
<h4 class="abs footer-head" style="left:63.4px;top:1130px">LanePilot</h4>
<p class="abs footer-text" style="left:63.4px;top:1155.4px;width:112px">AI-powered solutions designed specifically to help driving schools automate</p>

<h4 class="abs footer-head" style="left:189.6px;top:1130px">Solutions</h4>
<span class="abs footer-link" style="left:189.6px;top:1156px">Voice Agent</span>
<span class="abs footer-link" style="left:189.6px;top:1175.5px">AI Chat Assistant</span>
<span class="abs footer-link" style="left:189.6px;top:1195px">Document Processing</span>

<h4 class="abs footer-head" style="left:315.8px;top:1130px">Company</h4>
<span class="abs footer-link" style="left:315.8px;top:1156px">About Us</span>
<span class="abs footer-link" style="left:315.8px;top:1175.5px">Careers</span>
<span class="abs footer-link" style="left:315.8px;top:1195px">Blog</span>

<h4 class="abs footer-head" style="left:441.6px;top:1130px">Resources</h4>
<span class="abs footer-link" style="left:441.6px;top:1156px">FAQ</span>
<span class="abs footer-link" style="left:441.6px;top:1175.5px">Support</span>
<span class="abs footer-link" style="left:441.6px;top:1195px">Case Studies</span>

<h4 class="abs footer-head" style="left:567.8px;top:1130px">Contact</h4>
<span class="abs footer-contact" style="left:567.8px;top:1156px">48 Lumen Way</span>
<span class="abs footer-contact" style="left:567.8px;top:1175.5px">Brookvale, CA 94310</span>
<span class="abs footer-contact" style="left:567.8px;top:1195px">hello@lanepilot.example</span>

</body>
</html>
```